Prepared Meal Company Needs Menu Design

We are a pre-prepared meal delivery company called Grubb Larderly.

We have a menu in excel but needs to be designed to look good and appealing to customers. The menu should be clean, easy to ready, and show:Title (Pupusa)Tags (V, V+, GF - Use a cool vegan logo for the V+ and logo for vegetarian V symbol)Price (12.99)DescriptionBrand colors are orange white and green. Design is clean, crisp and can incorporate natural elements like leaf shaped symbols, etc. Screenshots from our website attached for inspiration.

Target Market(s)

Broad demographics

Industry/Entity Type

Restaurant

Font styles to use
Sans Serif

Requirements
Must have
• The menu design should be commensurate with the website under development
• https://grubblarderly.dishsite.example
Nice to have
• Should have appropriate graphics
Should not have
• Modifiers do not need to be shown (these are shown in the excel only).

```html
<!DOCTYPE html>
<html lang="en">
<head>
<meta charset="utf-8">
<title>Grubb Larderly Menu</title>
<link href="https://fonts.googleapis.com/css2?family=Nunito:wght@700;800&family=Open+Sans:wght@400;600&family=Roboto+Condensed:wght@700&display=swap" rel="stylesheet">
<style>
:root{
  --bg:#ede4df;
  --paper:#f6f5f0;
  --orange:#e2641c;
  --green:#2f7d32;
  --leaf:#7fa06a;
  --ink:#333;
  --muted:#555;
  --peach:#f9e2cf;
  --numeral:#e3e1dc;
}
*{box-sizing:border-box;margin:0;padding:0}
html,body{width:1033px;height:1200px;overflow:hidden}
body{background:var(--bg);font-family:"Open Sans",sans-serif;color:var(--ink)}
.spread{position:absolute;left:16px;width:1001px;height:575px;display:flex;gap:1px;box-shadow:0 4px 14px rgba(0,0,0,.12)}
.spread--top{top:14px}
.spread--bottom{top:610px}
.page{position:relative;width:500px;height:575px;background:var(--paper);overflow:hidden}
.page--left{padding:44px 58px 0 78px}
.page--right{padding:44px 70px 0 62px}
.decor{position:absolute;border-radius:50%;opacity:.55;filter:blur(1px)}
.decor--leaf{background:radial-gradient(ellipse at center,#8fae7c 0%,#b9cca7 45%,rgba(246,245,240,0) 72%)}
.decor--autumn{background:radial-gradient(ellipse at center,#e0a05a 0%,#efc99a 45%,rgba(246,245,240,0) 72%)}
.content{position:relative;z-index:1}
.item{margin-bottom:13px}
.item-name{display:flex;align-items:center;gap:4px;font:800 13px "Nunito",sans-serif;color:var(--orange)}
.item-note{font:600 7px "Open Sans",sans-serif;color:var(--green);margin-top:-1px}
.item-line{display:flex;align-items:flex-end;margin-top:3px}
.item-desc{font-size:8.5px;line-height:1.45;color:var(--muted);max-width:250px}
.leader{flex:1;border-bottom:1px dotted #777;margin:0 10px 4px;min-width:30px}
.price{font:700 14px "Roboto Condensed",sans-serif;color:var(--ink)}
.icon{width:13px;height:13px;flex:none}
.section-title{display:flex;justify-content:center;margin:22px 0 20px}
.section-title span{font:700 21px "Roboto Condensed",sans-serif;letter-spacing:3px;color:#2b2b2b;padding:5px 26px;border:1.5px solid #444;clip-path:polygon(4% 0,96% 0,100% 50%,96% 100%,4% 100%,0 50%)}
.band{background:var(--peach);margin:0 -18px;padding:12px 18px 2px}
.legend{position:absolute;bottom:40px;display:flex;gap:14px;padding-top:8px;border-top:1px dashed var(--orange);font-size:7px;color:var(--muted);z-index:1}
.legend span{display:flex;align-items:center;gap:3px}
.legend .icon{width:11px;height:11px}
.page--left .legend{left:62px}
.page--right .legend{right:50px}
.folio{position:absolute;bottom:-4px;font:700 96px "Roboto Condensed",sans-serif;color:var(--numeral);line-height:1}
.page--left .folio{right:20px}
.page--right .folio{left:30px}
</style>
</head>
<body>
<svg width="0" height="0" style="position:absolute" aria-hidden="true">
  <defs>
    <symbol id="i-vegan" viewBox="0 0 14 14"><path d="M2 3 L6 12 L12 1" fill="none" stroke="#2f7d32" stroke-width="1.8" stroke-linecap="round"/><path d="M9 4 q3-3 4-2 q-1 3-4 2z" fill="#2f7d32"/></symbol>
    <symbol id="i-veg" viewBox="0 0 14 14"><path d="M1 8 Q4 1 13 4 Q10 12 1 8z" fill="#2f7d32"/><path d="M2 8 Q7 6 12 4.5" stroke="#f6f5f0" stroke-width=".8" fill="none"/></symbol>
    <symbol id="i-gf" viewBox="0 0 14 14"><circle cx="7" cy="7" r="6" fill="none" stroke="#2f7d32" stroke-width="1.2"/><path d="M7 3 v8 M5 5 l2 1.5 l2-1.5 M5 8 l2 1.5 l2-1.5" stroke="#e2641c" stroke-width="1" fill="none"/><path d="M3.5 10.5 L10.5 3.5" stroke="#e2641c" stroke-width="1"/></symbol>
    <symbol id="i-df" viewBox="0 0 14 14"><circle cx="7" cy="7" r="6" fill="none" stroke="#2f7d32" stroke-width="1.2"/><path d="M5.5 4 h3 v1.5 l1 1.5 v4 h-5 v-4 l1-1.5z" fill="none" stroke="#e2641c" stroke-width="1"/><path d="M3.5 10.5 L10.5 3.5" stroke="#e2641c" stroke-width="1"/></symbol>
  </defs>
</svg>

<!-- Spread 07 / 08 -->
<section class="spread spread--top">
  <article class="page page--left">
    <div class="decor decor--leaf" style="left:-10px;top:-30px;width:170px;height:90px" role="img" aria-label="Watercolour leafy branch"></div>
    <div class="decor decor--leaf" style="left:-40px;bottom:-20px;width:150px;height:140px" role="img" aria-label="Watercolour leaves"></div>
    <div class="content">
      <div class="item">
        <div class="item-name">California Sunshine Flatbread <svg class="icon"><use href="#i-veg"/></svg><svg class="icon"><use href="#i-gf"/></svg></div>
        <div class="item-line"><p class="item-desc">{ Roasted Cherry Tomato, Asparagus &amp; Arugula, Chevre, Crisped Inca Corn, Poached Egg on Handmade Gluten-Free Flatbread }</p><span class="leader"></span><span class="price">$10.99</span></div>
      </div>
      <div class="item">
        <div class="item-name">Bison Shortrib &amp; Creamy Mushroom Flatbread <svg class="icon"><use href="#i-gf"/></svg></div>
        <div class="item-line"><p class="item-desc">{ Goat Cheese, Sugar Snap Peas, Radish, Roasted Garlic &amp; Mushroom Sauce on Handmade Gluten-Free Flatbread }</p><span class="leader"></span><span class="price">$13.99</span></div>
      </div>
      <div class="item">
        <div class="item-name">Marinated Squash Flatbread <svg class="icon"><use href="#i-veg"/></svg><svg class="icon"><use href="#i-gf"/></svg></div>
        <div class="item-line"><p class="item-desc">{ Chayote Escabeche, Avocado, Pepitas, Ancho Oil, Cilantro &amp; Inca Corn Crumble on Handmade Gluten-Free Flatbread }</p><span class="leader"></span><span class="price">$9.49</span></div>
      </div>
      <div class="section-title"><span>SNACKS/SIDES</span></div>
      <div class="item">
        <div class="item-name">Carrots &amp; Almond Butter <svg class="icon"><use href="#i-veg"/></svg><svg class="icon"><use href="#i-gf"/></svg><svg class="icon"><use href="#i-df"/></svg><svg class="icon"><use href="#i-vegan"/></svg></div>
        <div class="item-note">[ * if No Honey ]</div>
        <div class="item-line"><p class="item-desc">{ Dried Cranberries, Raw Honey, Black Sesame Seeds &amp; Marlow Sea Salt }</p><span class="leader"></span><span class="price">$5.99</span></div>
      </div>
      <div class="item">
        <div class="item-name">6" Corn Tortilla <svg class="icon"><use href="#i-vegan"/></svg><svg class="icon"><use href="#i-gf"/></svg></div>
        <div class="item-line"><p class="item-desc">{ Handmade Corn Tortillas }</p><span class="leader"></span><span class="price">$1.49</span></div>
      </div>
      <div class="item">
        <div class="item-name">Handmade Gluten-Free Flatbread <svg class="icon"><use href="#i-veg"/></svg><svg class="icon"><use href="#i-gf"/></svg></div>
        <div class="item-line"><p class="item-desc">{ Garden Herb Oil, Sumac, Pistachio &amp; Thyme }</p><span class="leader"></span><span class="price">$4.99</span></div>
      </div>
    </div>
    <div class="legend"><span><svg class="icon"><use href="#i-vegan"/></svg>Vegan</span><span><svg class="icon"><use href="#i-gf"/></svg>Gluten Free</span><span><svg class="icon"><use href="#i-veg"/></svg>Vegetarian</span><span><svg class="icon"><use href="#i-df"/></svg>Dairy Free</span></div>
    <div class="folio">07</div>
  </article>

  <article class="page page--right">
    <div class="decor decor--leaf" style="left:80px;top:-30px;width:110px;height:80px" role="img" aria-label="Watercolour leaves with a small bird"></div>
    <div class="decor decor--autumn" style="right:-20px;top:-10px;width:130px;height:90px" role="img" aria-label="Watercolour autumn leaves"></div>
    <div class="decor decor--leaf" style="right:-40px;top:170px;width:130px;height:150px" role="img" aria-label="Watercolour leafy branch"></div>
    <div class="decor decor--leaf" style="right:-40px;bottom:30px;width:120px;height:200px" role="img" aria-label="Watercolour leaves and blossoms"></div>
    <div class="content">
      <div class="item">
        <div class="item-name">Polenta Cake <svg class="icon"><use href="#i-veg"/></svg><svg class="icon"><use href="#i-gf"/></svg><svg class="icon"><use href="#i-df"/></svg><svg class="icon"><use href="#i-vegan"/></svg></div>
        <div class="item-note">[ * if No Honey ]</div>
        <div class="item-line"><p class="item-desc">{ Fairhollow Farms Lavender Honey, Rosemary, Sea Salt }</p><span class="leader"></span><span class="price">$3.99</span></div>
      </div>
      <div class="item">
        <div class="item-name">Guacamole <svg class="icon"><use href="#i-vegan"/></svg><svg class="icon"><use href="#i-gf"/></svg></div>
        <div class="item-line"><p class="item-desc">{ Chilaca Chile, Red Onion, Jalapeno, Tomato, Cilantro, Lime &amp; Marlow Sea Salt }</p><span class="leader"></span><span class="price">$4.99</span></div>
      </div>
      <div class="item">
        <div class="item-name">Soft Yolk Egg <svg class="icon"><use href="#i-veg"/></svg><svg class="icon"><use href="#i-gf"/></svg><svg class="icon"><use href="#i-df"/></svg></div>
        <div class="item-line"><p class="item-desc">{ Whole Sous Vide Egg }</p><span class="leader"></span><span class="price">$4.99</span></div>
      </div>
      <div class="item">
        <div class="item-name">Ayocote Beans <svg class="icon"><use href="#i-vegan"/></svg><svg class="icon"><use href="#i-gf"/></svg></div>
        <div class="item-line"><p class="item-desc">{ Rancho Verdal Heirloom Oaxacan Beans w/ Aromatics &amp; Epazote }</p><span class="leader"></span><span class="price">$6.99</span></div>
      </div>
      <div class="item">
        <div class="item-name">Moroccan Red Lentil &amp; Sorghum Patty <svg class="icon"><use href="#i-vegan"/></svg><svg class="icon"><use href="#i-gf"/></svg></div>
        <div class="item-line"><p class="item-desc">{ Red Lentils, Sorghum, Carrots, Onions, Bell Pepper, Guajillo Chile, Cumin, Cardamom, Coriander &amp; Clove }</p><span class="leader"></span><span class="price">$4.99</span></div>
      </div>
      <div class="item">
        <div class="item-name">Hazel's Grilled Chicken <svg class="icon"><use href="#i-gf"/></svg><svg class="icon"><use href="#i-df"/></svg></div>
        <div class="item-line"><p class="item-desc">{ Free Range Ground Turkey, Oregano &amp; Sumac }</p><span class="leader"></span><span class="price">$4.99</span></div>
      </div>
      <div class="item">
        <div class="item-name">Free Range Turkey Meatballs <svg class="icon"><use href="#i-gf"/></svg><svg class="icon"><use href="#i-df"/></svg></div>
        <div class="item-line"><p class="item-desc">{ Free Range Ground Turkey, Oregano &amp; Sumac }</p><span class="leader"></span><span class="price">$4.99</span></div>
      </div>
      <div class="item">
        <div class="item-name">Pacific Ocean Perch Filet <svg class="icon"><use href="#i-gf"/></svg><svg class="icon"><use href="#i-df"/></svg></div>
        <div class="item-line"><p class="item-desc">{ Pan Seared Pacific Ocean Perch Filet }</p><span class="leader"></span><span class="price">$6.99</span></div>
      </div>
    </div>
    <div class="legend"><span><svg class="icon"><use href="#i-vegan"/></svg>Vegan</span><span><svg class="icon"><use href="#i-gf"/></svg>Gluten Free</span><span><svg class="icon"><use href="#i-veg"/></svg>Vegetarian</span><span><svg class="icon"><use href="#i-df"/></svg>Dairy Free</span></div>
    <div class="folio">08</div>
  </article>
</section>

<!-- Spread 09 / 10 -->
<section class="spread spread--bottom">
  <article class="page page--left">
    <div class="decor decor--leaf" style="left:-20px;top:-30px;width:160px;height:100px" role="img" aria-label="Watercolour leafy branch"></div>
    <div class="decor decor--leaf" style="left:-40px;bottom:10px;width:120px;height:220px" role="img" aria-label="Watercolour leaves and blossoms"></div>
    <div class="content">
      <div class="item">
        <div class="item-name">Salmon Patty <svg class="icon"><use href="#i-df"/></svg></div>
        <div class="item-line"><p class="item-desc">{ Scottish Salmon, Spinach &amp; Lemon }</p><span class="leader"></span><span class="price">$6.99</span></div>
      </div>
      <div class="item">
        <div class="item-name">Salmon Filet <svg class="icon"><use href="#i-gf"/></svg><svg class="icon"><use href="#i-df"/></svg></div>
        <div class="item-line"><p class="item-desc">{ Pan Seared Filet of Scottish Salmon }</p><span class="leader"></span><span class="price">$7.99</span></div>
      </div>
      <div class="item">
        <div class="item-name">Tropical Acai Hot Sauce <svg class="icon"><use href="#i-vegan"/></svg><svg class="icon"><use href="#i-gf"/></svg></div>
        <div class="item-line"><p class="item-desc">{ Pomegranate, Strawberry, Guajillo, Jalapeno &amp; Lime }</p><span class="leader"></span><span class="price">$2.49</span></div>
      </div>
      <div class="item">
        <div class="item-name">Chayote Escabeche <svg class="icon"><use href="#i-vegan"/></svg><svg class="icon"><use href="#i-gf"/></svg></div>
        <div class="item-line"><p class="item-desc">{ Chayote Squash, Jalapeno, Extra Virgin Olive Oil &amp; Lemon }</p><span class="leader"></span><span class="price">$2.49</span></div>
      </div>
      <div class="item">
        <div class="item-name">Monkfruit &amp; Balsamic Glaze <svg class="icon"><use href="#i-vegan"/></svg><svg class="icon"><use href="#i-gf"/></svg></div>
        <div class="item-line"><p class="item-desc">{ Balsamic Vinager sweetened &amp; reduced with Monkfruit }</p><span class="leader"></span><span class="price">$1.79</span></div>
      </div>
      <div class="item">
        <div class="item-name">Salsa Roja <svg class="icon"><use href="#i-vegan"/></svg><svg class="icon"><use href="#i-gf"/></svg></div>
        <div class="item-line"><p class="item-desc">{ Guajillo, Ancho &amp; Tomato }</p><span class="leader"></span><span class="price">$1.29</span></div>
      </div>
      <div class="band">
        <div class="item">
          <div class="item-name">Manzanilla Yogurt <svg class="icon"><use href="#i-veg"/></svg><svg class="icon"><use href="#i-gf"/></svg></div>
          <div class="item-line"><p class="item-desc">{ Greek Yogurt with Honey, Roman Chamomile &amp; Lemon }</p><span class="leader"></span><span class="price">$1.39</span></div>
        </div>
        <div class="item">
          <div class="item-name">Cilantro-Lime Yogurt <svg class="icon"><use href="#i-veg"/></svg><svg class="icon"><use href="#i-gf"/></svg></div>
          <div class="item-line"><p class="item-desc">{ Greek Yogurt with Cilantro, Lime, Honey &amp; Cumin }</p><span class="leader"></span><span class="price">$1.69</span></div>
        </div>
        <div class="item">
          <div class="item-name">Saffron &amp; Chamomile Yogurt <svg class="icon"><use href="#i-veg"/></svg><svg class="icon"><use href="#i-gf"/></svg></div>
          <div class="item-line"><p class="item-desc">{ Greek Yogurt with Saffron, Chamomile, Honey &amp; Citrus }</p><span class="leader"></span><span class="price">$1.99</span></div>
        </div>
      </div>
    </div>
    <div class="legend"><span><svg class="icon"><use href="#i-vegan"/></svg>Vegan</span><span><svg class="icon"><use href="#i-gf"/></svg>Gluten Free</span><span><svg class="icon"><use href="#i-veg"/></svg>Vegetarian</span><span><svg class="icon"><use href="#i-df"/></svg>Dairy Free</span></div>
    <div class="folio">09</div>
  </article>

  <article class="page page--right">
    <div class="decor decor--leaf" style="left:200px;top:-30px;width:280px;height:110px" role="img" aria-label="Watercolour leafy branches"></div>
    <div class="decor decor--leaf" style="right:-40px;top:60px;width:110px;height:160px" role="img" aria-label="Watercolour leaves"></div>
    <div class="decor decor--leaf" style="right:-30px;bottom:-10px;width:120px;height:120px" role="img" aria-label="Watercolour leaves and a yellow flower"></div>
    <div class="content">
      <div class="item">
        <div class="item-name">Cider Vinaigrette <svg class="icon"><use href="#i-veg"/></svg><svg class="icon"><use href="#i-gf"/></svg><svg class="icon"><use href="#i-df"/></svg></div>
        <div class="item-line"><p class="item-desc">{ Arbequina Olive Oil, Apple Cider Vinager &amp; Raw Honey }</p><span class="leader"></span><span class="price">$2.29</span></div>
      </div>
      <div class="item">
        <div class="item-name">Carrot-Ginger Vinaigrette <svg class="icon"><use href="#i-veg"/></svg><svg class="icon"><use href="#i-gf"/></svg><svg class="icon"><use href="#i-df"/></svg></div>
        <div class="item-line"><p class="item-desc">{ Raw Honey, Carrot, Ginger, Olive Oil &amp; Vinager }</p><span class="leader"></span><span class="price">$1.39</span></div>
      </div>
      <div class="item">
        <div class="item-name">Golden Valley Olive Ranch Arbequina Extra Virgin Olive Oil <svg class="icon"><use href="#i-vegan"/></svg><svg class="icon"><use href="#i-gf"/></svg></div>
        <div class="item-line"><p class="item-desc">{ Golden Valley Arbequina Extra Virgin Olive Oil }</p><span class="leader"></span><span class="price">$1.99</span></div>
      </div>
      <div class="band">
        <div class="item">
          <div class="item-name">Goat Cheese <svg class="icon"><use href="#i-veg"/></svg><svg class="icon"><use href="#i-gf"/></svg><span class="leader"></span><span class="price">$2.99</span></div>
        </div>
        <div class="item">
          <div class="item-name">Lemon Juice <svg class="icon"><use href="#i-vegan"/></svg><svg class="icon"><use href="#i-gf"/></svg></div>
          <div class="item-line"><p class="item-desc">{ Pellarino Lemon Juice }</p><span class="leader"></span><span class="price">$0.75</span></div>
        </div>
        <div class="item">
          <div class="item-name">Lime Juice <svg class="icon"><use href="#i-vegan"/></svg><svg class="icon"><use href="#i-gf"/></svg></div>
          <div class="item-line"><p class="item-desc">{ Pellarino Lime Juice }</p><span class="leader"></span><span class="price">$0.75</span></div>
        </div>
        <div class="item">
          <div class="item-name">Almond Butter <svg class="icon"><use href="#i-vegan"/></svg><svg class="icon"><use href="#i-gf"/></svg><span class="leader"></span><span class="price">$4.49</span></div>
        </div>
        <div class="item">
          <div class="item-name">Raw Wildflower Honey <svg class="icon"><use href="#i-veg"/></svg><svg class="icon"><use href="#i-gf"/></svg><svg class="icon"><use href="#i-df"/></svg></div>
          <div class="item-line"><p class="item-desc">{ California Raw Wildflower Honey }</p><span class="leader"></span><span class="price">$2.99</span></div>
        </div>
        <div class="item">
          <div class="item-name">Lime Juice <svg class="icon"><use href="#i-vegan"/></svg><svg class="icon"><use href="#i-gf"/></svg></div>
          <div class="item-line"><p class="item-desc">{ Vegan Coconut Whipped Cream }</p><span class="leader"></span><span class="price">$2.49</span></div>
        </div>
      </div>
    </div>
    <div class="legend"><span><svg class="icon"><use href="#i-vegan"/></svg>Vegan</span><span><svg class="icon"><use href="#i-gf"/></svg>Gluten Free</span><span><svg class="icon"><use href="#i-veg"/></svg>Vegetarian</span><span><svg class="icon"><use href="#i-df"/></svg>Dairy Free</span></div>
    <div class="folio">10</div>
  </article>
</section>
</body>
</html>
```